Larkspire Benefits (03)

We're designing a website to sell Medicare Supplements. Attached is the script we want to say and general layout, but please use your best knowledge to make it better. This platform should be extremely user-friendly, but we want to make it look fun and approachable! Most Insurance/medicare websites are very boring, drab, simple but we want this one to be more personalized, fun and sexy (but again, still user-friendly since our target demographic is 65+).

This homepage should include a fun and inviting quiz, the script is in the attachment below. It should also include the blurbs about what medicare supplements plans are and why they should buy them. Feel free to play around with cool fonts and imagery, we want the site to be engaging!

Target Market(s)

seniors

Industry/Entity Type

Insurance

Number of Pages Required

1 page

Requirements
Must have
• Quiz, company name and tag line, script
Nice to have
• fun, engaging elements

```html
<!DOCTYPE html>
<html lang="en">
<head>
<meta charset="utf-8">
<title>Larkspire Benefits — Medicare Supplement Plans</title>
<link href="https://fonts.googleapis.com/css2?family=Quicksand:wght@500;600;700&family=Open+Sans:wght@400;600&family=Arimo:wght@400&display=swap" rel="stylesheet">
<style>
:root{
  --teal:#1e9cc6;
  --teal-deep:#0f86b3;
  --hero-blue:#22aed3;
  --orange:#e8561b;
  --quiz-start:#e8621a;
  --quiz-end:#e9b916;
  --ink:#222;
  --body:#555;
  --soft-bg:#eff1f5;
  --white:#fff;
}
*{box-sizing:border-box;margin:0;padding:0}
html,body{width:1200px;height:2942px;overflow:hidden;background:var(--white)}
body{position:relative;font-family:"Open Sans",sans-serif;color:var(--body)}

/* header */
.site-header{position:absolute;left:0;top:0;width:1200px;height:94px}
.brand{position:absolute;left:48px;top:30px;font:700 31px "Quicksand",sans-serif;color:var(--teal);letter-spacing:.3px}
.main-nav{position:absolute;right:54px;top:38px;display:flex;gap:41px;font:500 18px "Quicksand",sans-serif}
.main-nav a{color:var(--teal);text-decoration:none}
.main-nav a.current{color:#222;position:relative}
.main-nav a.current::after{content:"";position:absolute;left:12px;right:12px;bottom:-8px;height:2px;background:var(--teal)}

/* hero */
.hero{position:absolute;left:0;top:94px;width:1200px;height:566px;overflow:hidden}
.hero-photo{position:absolute;inset:0;background:linear-gradient(100deg,#6e7b84 0%,#c8c6c2 45%,#e8e6e2 70%,#bfc3c6 100%)}
.hero-shape{position:absolute;left:0;top:0}
.hero-title{position:absolute;left:91px;top:152px;font:700 48px "Quicksand",sans-serif;color:var(--white);letter-spacing:.5px}
.hero-tagline{position:absolute;left:94px;top:220px;font:500 24px/32px "Quicksand",sans-serif;color:var(--white)}
.call-btn{position:absolute;left:85px;top:306px;width:361px;height:60px;border-radius:30px;background:var(--orange);color:var(--white);display:flex;align-items:center;justify-content:center;gap:6px;font:700 28px "Quicksand",sans-serif;box-shadow:0 3px 6px rgba(0,0,0,.15)}
.hero-note{position:absolute;left:114px;top:380px;font:700 20px "Quicksand",sans-serif;color:var(--white);letter-spacing:.3px}

/* intro */
.intro{position:absolute;left:0;top:748px;width:1200px;text-align:center;font:400 21px/35px "Arimo",sans-serif;color:#444}
.intro-cta{position:absolute;left:0;top:845px;width:1200px;text-align:center;font:400 21px/29px "Arimo",sans-serif;color:#111}

/* quiz */
.quiz{position:absolute;left:0;top:993px;width:1200px;height:516px;background:linear-gradient(90deg,var(--quiz-start) 0%,#ea8a18 50%,var(--quiz-end) 100%);overflow:hidden}
.quiz::before{content:"";position:absolute;inset:0;background:radial-gradient(ellipse at 40% 40%,rgba(120,60,20,.18),transparent 60%)}
.quiz-notch{position:absolute;left:582px;top:0;width:0;height:0;border-left:19px solid transparent;border-right:19px solid transparent;border-top:23px solid var(--white)}
.quiz-title{position:absolute;left:0;top:60px;width:1200px;text-align:center;font:700 40px "Quicksand",sans-serif;color:var(--white)}
.quiz-col{position:absolute;top:142px;color:var(--white);font-family:"Arimo",sans-serif}
.quiz-col h3{font-weight:400;font-size:24px;margin-bottom:14px;padding-left:1px}
.quiz-option{display:flex;align-items:center;gap:11px;font-size:20px;height:40px}
.quiz-option span.box{width:23px;height:22px;background:var(--white);flex:none}
.zip-field{position:absolute;left:318px;top:364px;width:558px;height:65px;background:var(--white);display:flex;align-items:center;padding-left:18px;gap:14px;font:400 20px "Arimo",sans-serif;color:#222}

/* what is */
.section-title{position:absolute;left:0;width:1200px;text-align:center;font:500 33px "Quicksand",sans-serif;color:var(--ink)}
.lead{position:absolute;left:172px;width:856px;text-align:center;font:400 17px/27px "Open Sans",sans-serif;color:var(--body)}
.benefit{position:absolute;display:flex;gap:8px;font:400 17px/27px "Open Sans",sans-serif;color:var(--body)}
.benefit svg{flex:none;margin-top:6px}

/* costs */
.costs{position:absolute;left:0;top:2015px;width:1200px;height:733px;background:var(--soft-bg)}
.costs-title{position:absolute;left:0;top:64px;width:1200px;text-align:center;font:700 34px "Quicksand",sans-serif;color:var(--teal)}
.costs-lead{position:absolute;left:150px;top:120px;width:900px;text-align:center;font:400 17.5px/27.5px "Open Sans",sans-serif;color:#444}
.rating-card{position:absolute;top:281px;width:370px;height:306px;background:var(--white);border-radius:6px;box-shadow:0 2px 10px rgba(0,0,0,.08);text-align:center}
.rating-card svg{position:absolute;left:153px;top:36px}
.rating-card h4{position:absolute;left:0;right:0;top:134px;font:700 20px "Quicksand",sans-serif;color:#222;letter-spacing:.3px}
.rating-card p{position:absolute;left:40px;right:40px;top:174px;font:400 13.5px/23px "Open Sans",sans-serif;color:#555}
.costs-note{position:absolute;left:0;top:640px;width:1200px;text-align:center;font:400 16px/24px "Open Sans",sans-serif;color:#555}

/* footer */
.footer-nav{position:absolute;left:0;top:2792px;width:1200px;display:flex;justify-content:center;gap:44px;font:500 18px "Quicksand",sans-serif;color:#222}
.footer-nav a{color:inherit;text-decoration:none}
.legal{position:absolute;left:0;top:2834px;width:1200px;text-align:center;font:400 14px "Open Sans",sans-serif;color:#222}
.social{position:absolute;left:505px;top:2874px;display:flex;gap:6px}
.social span{width:41px;height:41px;border:2px solid #1c5fa8;border-radius:50%}
</style>
</head>
<body>

<header class="site-header">
  <div class="brand">Larkspire Benefits</div>
  <nav class="main-nav">
    <a class="current" href="#">About</a>
    <a href="#">Our Quiz</a>
    <a href="#">Supplement Plan</a>
    <a href="#">Blog</a>
    <a href="#">Why Us</a>
    <a href="#">Contact</a>
  </nav>
</header>

<section class="hero">
  <div class="hero-photo" role="img" aria-label="Photo of a smiling young woman sitting cross-legged with a laptop in a bright living room"></div>
  <svg class="hero-shape" width="640" height="566" viewBox="0 0 640 566" aria-hidden="true">
    <defs>
      <linearGradient id="heroBlue" x1="0" y1="0" x2="1" y2="0">
        <stop offset="0" stop-color="#17a4cf"/>
        <stop offset="1" stop-color="#2bb6d8"/>
      </linearGradient>
    </defs>
    <path d="M0 0 H500 C600 90 650 260 600 410 C580 470 545 525 488 566 H0 Z" fill="url(#heroBlue)" opacity=".96"/>
  </svg>
  <h1 class="hero-title">Larkspire Benefits</h1>
  <p class="hero-tagline">Be confident in choosing the Medicare<br>Supplement plan that’s right for you.</p>
  <div class="call-btn">
    <svg width="26" height="26" viewBox="0 0 24 24" aria-hidden="true"><path d="M6.6 10.8a15 15 0 0 0 6.6 6.6l2.2-2.2a1 1 0 0 1 1-.25 11.4 11.4 0 0 0 3.6.57 1 1 0 0 1 1 1V20a1 1 0 0 1-1 1A17 17 0 0 1 3 4a1 1 0 0 1 1-1h3.5a1 1 0 0 1 1 1c0 1.25.2 2.45.57 3.57a1 1 0 0 1-.25 1z" fill="#fff"/><path d="M14 3a7 7 0 0 1 7 7M14 6.5a3.5 3.5 0 0 1 3.5 3.5" stroke="#fff" stroke-width="1.8" fill="none" stroke-linecap="round"/></svg>
    Call (800) 555-0148
  </div>
  <p class="hero-note">to talk to a live agent.</p>
</section>

<p class="intro">We know insurance can be confusing. With so much information and not enough answers, we’re here<br>to help you find the plan that works best for you, your family and your health.</p>
<p class="intro-cta">Take this short quiz to to find flexible and affordable plans<br>that you can feel confident in.</p>

<section class="quiz" role="img" aria-label="Warm orange-tinted photo of a smiling senior couple behind the quiz">
  <div class="quiz-notch"></div>
  <h2 class="quiz-title">Quiz Script</h2>
  <div class="quiz-col" style="left:178px">
    <h3>I am</h3>
    <div class="quiz-option"><span class="box"></span>a. Over 64 years old</div>
    <div class="quiz-option"><span class="box"></span>b. 64 years old</div>
    <div class="quiz-option"><span class="box"></span>c. Under 64 years old</div>
  </div>
  <div class="quiz-col" style="left:546px">
    <h3>I am</h3>
    <div class="quiz-option"><span class="box"></span>a. Male</div>
    <div class="quiz-option"><span class="box"></span>b. Female</div>
    <div class="quiz-option"><span class="box"></span>c. Unspecified</div>
  </div>
  <div class="quiz-col" style="left:858px">
    <h3>I want to see</h3>
    <div class="quiz-option"><span class="box"></span>a. Free plans</div>
    <div class="quiz-option"><span class="box"></span>b. Premium plans</div>
    <div class="quiz-option"><span class="box"></span>c. All plans</div>
  </div>
  <div class="zip-field">
    <svg width="22" height="30" viewBox="0 0 22 30" aria-hidden="true"><path d="M11 0C5 0 0 4.7 0 10.6 0 18 11 30 11 30s11-12 11-19.4C22 4.7 17 0 11 0z" fill="#999"/><circle cx="11" cy="10.5" r="4" fill="#fff"/></svg>
    Enter Zip Code
  </div>
</section>

<h2 class="section-title" style="top:1604px">What is a Medicare Supplement plan?</h2>
<p class="lead" style="top:1662px">Each Medicare Supplement insurance plan offers a different level of basic benefits, but each lettered plan will include the same standardized basic benefits regardless of insurance company and location. Medicare Supplement insurance plans do not always cover vision, dental, long-term care, or hearing aids, but all plans must cover at least a portion of the following basic benefits:</p>

<div class="benefit" style="left:106px;top:1812px;width:520px">
  <svg width="24" height="16" viewBox="0 0 24 16" aria-hidden="true"><path d="M2 8l6 6L22 2" stroke="#f0901a" stroke-width="3" fill="none" stroke-linecap="round"/></svg>
  <span>Medicare Part A coinsurance costs up to an additional 365 days after Medicare benefits are exhausted</span>
</div>
<div class="benefit" style="left:110px;top:1880px;width:520px">
  <svg width="24" height="16" viewBox="0 0 24 16" style="margin-top:14px" aria-hidden="true"><path d="M2 8l6 6L22 2" stroke="#f0901a" stroke-width="3" fill="none" stroke-linecap="round"/></svg>
  <span>Medicare Part A hospice care coinsurance or copayments</span>
</div>
<div class="benefit" style="left:656px;top:1812px;width:480px">
  <svg width="24" height="16" viewBox="0 0 24 16" aria-hidden="true"><path d="M2 8l6 6L22 2" stroke="#f0901a" stroke-width="3" fill="none" stroke-linecap="round"/></svg>
  <span>Medicare Part B coinsurance or copayments</span>
</div>
<div class="benefit" style="left:656px;top:1874px;width:480px">
  <svg width="24" height="16" viewBox="0 0 24 16" aria-hidden="true"><path d="M2 8l6 6L22 2" stroke="#f0901a" stroke-width="3" fill="none" stroke-linecap="round"/></svg>
  <span>First three pints of blood used in a medical procedure</span>
</div>

<section class="costs">
  <h2 class="costs-title">Medicare Supplement insurance plan costs</h2>
  <p class="costs-lead">Although private insurance companies are required to offer the same basic benefits for each lettered plan, they do have the ability to charge different premiums. You might want to shop around to find a Medicare Supplement insurance plan that may fit your medical and financial needs. Insurance companies may price their plan premiums in any of the following ways:</p>

  <article class="rating-card" style="left:26px">
    <svg width="64" height="64" viewBox="0 0 64 64" fill="none" stroke="#1e9cc6" stroke-width="2" stroke-linecap="round" aria-hidden="true">
      <circle cx="32" cy="12" r="5"/><circle cx="22" cy="18" r="4"/><circle cx="42" cy="18" r="4"/>
      <path d="M24 30c0-6 16-6 16 0M16 30c0-5 10-6 12-3M48 30c0-5-10-6-12-3"/>
      <path d="M6 26c-2 10 2 20 12 30h8v-10l-8-8M58 26c2 10-2 20-12 30h-8v-10l8-8"/>
    </svg>
    <h4>Community no-age-rated</h4>
    <p style="left:36px;right:36px">These Medicare Supplement insurance plans charge premiums that are the same across the board, regardless of age.</p>
  </article>

  <article class="rating-card" style="left:415px">
    <svg width="64" height="64" viewBox="0 0 64 64" fill="none" stroke="#1e9cc6" stroke-width="2" stroke-linecap="round" aria-hidden="true">
      <circle cx="36" cy="10" r="5"/><path d="M26 26c0-8 20-8 20 0"/><rect x="22" y="4" width="28" height="26" rx="2"/>
      <rect x="4" y="34" width="20" height="26"/><path d="M8 42h12M8 48h12M8 54h8"/>
      <circle cx="48" cy="48" r="8"/><circle cx="48" cy="48" r="3"/><path d="M28 48h10M31 45l-3 3 3 3M14 30v-6h8"/>
    </svg>
    <h4 style="top:130px">Issue-age-rated</h4>
    <p style="top:170px">These plans base their premiums on your age when you first enrolled in the policy. Therefore, the younger you are when you enroll in this type of plan, the lower your premium will be.</p>
  </article>

  <article class="rating-card" style="left:804px">
    <svg width="64" height="64" viewBox="0 0 64 64" fill="none" stroke="#1e9cc6" stroke-width="2" stroke-linecap="round" aria-hidden="true">
      <rect x="22" y="4" width="30" height="40" rx="2"/><rect x="28" y="12" width="30" height="46" rx="2"/>
      <path d="M34 22h18M34 28h18M34 34h18M34 40h12"/>
      <path d="M18 24l12 4v10c0 8-6 13-12 16-6-3-12-8-12-16V28z"/><path d="M13 39l4 4 7-8"/>
    </svg>
    <h4 style="top:130px">Attained-age-rated</h4>
    <p style="top:170px;left:38px;right:28px">Like issue-age-rated, these plans base their premiums on the age you were when you first bought a policy, but unlike issue-age-rated, premiums increase as you get older.</p>
  </article>

  <p class="costs-note">Please note that no matter what rating method an insurance company uses, premiums<br>may increase over time for reasons other than age, such as inflation.</p>
</section>

<footer>
  <nav class="footer-nav">
    <a href="#">About</a><a href="#">Our Quiz</a><a href="#">Supplement Plan</a><a href="#">Blog</a><a href="#">Why Us</a><a href="#">Contact</a>
  </nav>
  <p class="legal">© 2020 Company Name | All Rights Reserved | Disclaimer</p>
  <div class="social" aria-label="Social media links">
    <span></span><span></span><span></span><span></span>
  </div>
</footer>

</body>
</html>
```